MRHT Needs Fundraiser Dinner Invite!!

The Marisol Hendrick Trust, a 501 3(c) non for profit has a yearly fundraiser, with varying themes. Last year it was "cowboys" and "cowgirls"
This year, it is Club Orchid, or 70's disco music. I have uploaded last years invite for reference, some stock photography for inspiration. You are not limited to using the stock photos.

Annual MRHT Fundraiser Dinner
October 13th, 2022
Starts: 6:30pm
RSVP By: September 20th
Place: The Bramwell
Price: $135 per ticket

Target Market(s)

Donors, Business People, Every person

Industry/Entity Type

Non for Profit

Font styles to use
Sans Serif

Colors
0054AA
0677BA
7BADD7
CADEEF
E8F1F8
E54698
E96AAD
F1A4CE
F9D9EA
FCEFF6
6B429C
8869AF
B7A5CE
E3DAEB
F3F0F8

Requirements
Must have
• The invite should be 5x7, be sophisticated as the clientele are mainly business people that come to support the cause. It should be fun and inviting at the same time.

```html
<!DOCTYPE html>
<html lang="en">
<head>
<meta charset="utf-8">
<title>Let's Boogie! – MRHT Annual Fundraiser Dinner</title>
<link rel="stylesheet" href="https://fonts.googleapis.com/css2?family=Dela+Gothic+One&family=Righteous&family=Outfit:wght@300;600;700&display=swap">
<style>
  :root {
    --magenta: #E54698;
    --hot-pink: #FF74BF;
    --mid-pink: #EFA2CC;
    --blush: #F7D3F4;
    --plum: #5B3F78;
    --purple: #6B429C;
    --lilac: #8869AF;
    --star: #E3DAEB;
    --ink: #0A0A0A;
    --paper: #FFFFFF;
    --blue: #0677BA;
  }
  * { margin: 0; padding: 0; box-sizing: border-box; }
  html, body { width: 851px; height: 1200px; overflow: hidden; background: var(--magenta); }
  .invite {
    position: relative;
    width: 851px;
    height: 1200px;
    overflow: hidden;
    font-family: "Outfit", sans-serif;
  }
  .backdrop { position: absolute; inset: 0; }
  .headline {
    position: absolute;
    top: 80px;
    left: 0;
    width: 851px;
    height: 100px;
    margin: 0;
  }
  .headline svg { display: block; overflow: visible; }
  .headline-text {
    font-family: "Dela Gothic One", sans-serif;
    font-size: 92px;
    fill: var(--ink);
  }
  .dancer-art {
    position: absolute;
    left: 262px;
    top: 188px;
    width: 589px;
    height: 680px;
    border-radius: 40px 0 0 0;
    background:
      radial-gradient(ellipse at 55% 38%, rgba(243,240,248,0.95) 0%, rgba(243,240,248,0.55) 32%, rgba(243,240,248,0) 60%),
      linear-gradient(180deg, rgba(229,70,152,0) 0%, rgba(229,70,152,0) 55%, rgba(136,105,175,0.85) 78%, rgba(6,119,186,0.85) 100%);
  }
  .stars { position: absolute; inset: 0; pointer-events: none; }
  .star-label {
    font-family: "Righteous", sans-serif;
    fill: var(--plum);
    text-anchor: middle;
  }
  .details-card {
    position: absolute;
    left: 89px;
    top: 868px;
    width: 762px;
    height: 302px;
    background: var(--paper);
    border-radius: 14px 0 0 14px;
    display: flex;
    align-items: flex-start;
  }
  .details-card .col {
    text-align: center;
    padding-top: 40px;
  }
  .event-name { width: 381px; }
  .event-info { width: 380px; }
  .divider {
    width: 3px;
    height: 230px;
    margin-top: 41px;
    background: var(--ink);
  }
  .line {
    font-size: 27px;
    line-height: 38px;
    font-weight: 700;
    letter-spacing: -0.8px;
  }
  .line.dark { color: var(--ink); }
  .line.accent { color: var(--plum); }
  .line.light { font-weight: 300; color: var(--ink); }
  .org-mark {
    font-weight: 700;
    font-size: 108px;
    line-height: 100px;
    letter-spacing: -3px;
    color: var(--plum);
    margin: 4px 0 8px;
  }
</style>
</head>
<body>
<div class="invite">
  <svg class="backdrop" width="851" height="1200" viewBox="0 0 851 1200" aria-hidden="true">
    <rect width="851" height="1200" fill="var(--magenta)"/>
    <path fill="var(--plum)" d="M0,120 C70,60 150,10 250,0 L851,0 L851,1200 L0,1200 L0,1150 C50,1120 60,1060 40,1010 C20,960 0,940 0,900 Z"/>
    <path fill="var(--blush)" d="M0,270 C50,150 130,95 240,75 C380,50 470,95 570,62 C680,25 780,70 851,55 L851,880 L0,880 Z"/>
    <path fill="var(--mid-pink)" d="M30,430 C35,310 120,235 235,210 C345,185 425,205 525,172 C640,140 745,195 805,250 C835,280 851,300 851,320 L851,880 L45,880 C25,770 45,650 30,560 Z"/>
    <path fill="var(--hot-pink)" d="M62,570 C60,440 140,360 255,325 C375,290 460,305 560,282 C675,258 765,315 815,390 C845,440 851,470 851,500 L851,880 L78,880 C60,790 75,690 62,570 Z"/>
    <path fill="var(--magenta)" d="M148,650 C140,530 220,440 335,405 C460,368 565,385 665,425 C760,465 805,545 808,630 L808,880 L162,880 C148,800 160,725 148,650 Z"/>
  </svg>

  <h1 class="headline">
    <svg width="851" height="100" viewBox="0 0 851 100">
      <text class="headline-text" x="65" y="86" textLength="752" lengthAdjust="spacingAndGlyphs">LET'S BOOGIE!</text>
    </svg>
  </h1>

  <div class="dancer-art" role="img" aria-label="Illustration of a smiling disco dancer in a white suit and sunglasses pointing upward, dancing on a lit-up pink, purple and blue disco floor"></div>

  <svg class="stars" width="851" height="1200" viewBox="0 0 851 1200">
    <defs>
      <path id="star-shape" d="M0,-1 L.247,-.34 L.951,-.309 L.399,.13 L.588,.809 L0,.42 L-.588,.809 L-.399,.13 L-.951,-.309 L-.247,-.34 Z"/>
    </defs>
    <use href="#star-shape" fill="var(--star)" transform="translate(205,300) rotate(-12) scale(135)"/>
    <use href="#star-shape" fill="var(--star)" transform="translate(88,432) rotate(-14) scale(64)"/>
    <use href="#star-shape" fill="var(--star)" transform="translate(222,575) rotate(-12) scale(132)"/>
    <text class="star-label" font-size="27" transform="translate(205,300) rotate(-20)">Club</text>
    <text class="star-label" font-size="27" transform="translate(214,328) rotate(-20)">Orchid</text>
    <text class="star-label" font-size="38" transform="translate(228,570) rotate(-20)">$135</text>
    <text class="star-label" font-size="21" transform="translate(245,592) rotate(-20)">per</text>
    <text class="star-label" font-size="21" transform="translate(253,612) rotate(-20)">ticket</text>
  </svg>

  <section class="details-card">
    <div class="col event-name">
      <p class="line dark">You are invited to</p>
      <p class="line accent">Annual</p>
      <p class="org-mark">MRHT</p>
      <p class="line accent">Fundraiser Dinner</p>
    </div>
    <div class="divider"></div>
    <div class="col event-info">
      <p class="line accent">It's going to be fun and</p>
      <p class="line accent">70's disco music!</p>
      <p class="line dark">October 13th, 2022</p>
      <p class="line dark">at the Bramwell</p>
      <p class="line dark">doors open at 6:30 p.m.</p>
      <p class="line light">RSVP by September 20th</p>
    </div>
  </section>
</div>
</body>
</html>
```